Australian Natural Therpaist needs a light, fun, inviting wordpress website!

I need a wordpress website for my natural therapies business. I have already purchased the "vesk" theme from quillframestudio.com and so ideally this is what I would like to use.

The website will have the following pages:
1) Home
2) About Me
3) How I can help you
4) Contact Me
5) FAQ
6) Client Stories
7) Blog

I have attached a Balsamiq XML mockup and PDF of the homepage

I want the website to be very friendly and to de-mystify natural therapies/energy healing etc. I would like to keep the hand drawn/cartoon concept as it keeps everything light. My blog posts will consist of hand drawings and cartoons along with the blog text and so this would tie in with the look and feel of the website.

The homepage should have a slider at the top so that I can promote different concepts. The mockup shows an example of one of the advertising concepts I would use.

The website should make you feel light, it should be fun. No unicorns or rainbows. Here is a great example of what I DO NOT WANT http://www.copperwillowarts.com/

```html
<!DOCTYPE html>
<html lang="en">
<head>
<meta charset="utf-8">
<title>Lachlan Reeve — Healer, Helper, Mentor, Friend</title>
<link rel="stylesheet" href="https://fonts.googleapis.com/css2?family=Open+Sans:wght@400;600&display=swap">
<style>
:root{
  --ink:#1f1f1f;
  --text:#222;
  --muted:#555;
  --accent:#5bc2ee;
  --accent-dark:#3ea9d9;
  --icon:#6fb8f5;
  --icon-light:#b9dcfb;
  --more:#8a0a0a;
  --footer:#2c2c2c;
  --footer-text:#e6e6e6;
  --rule:#e2e2e2;
}
*{box-sizing:border-box;margin:0;padding:0}
html,body{width:1094px;height:1200px;overflow:hidden;background:#fff}
body{font-family:"Open Sans",Arial,sans-serif;color:var(--text);position:relative}
.site-header{position:absolute;top:0;left:0;width:1094px;height:80px}
.brand-name{position:absolute;left:101px;top:9px;font-size:28px;font-weight:600;color:var(--ink);letter-spacing:.2px}
.brand-tagline{position:absolute;left:104px;top:53px;font-size:13px;color:var(--ink);word-spacing:3px}
.main-nav{position:absolute;right:101px;top:55px;display:flex;gap:18px;font-size:12px}
.main-nav a{color:#444;text-decoration:none;position:relative;padding-bottom:9px}
.main-nav a.is-active{color:#333}
.main-nav a.is-active::after{content:"";position:absolute;left:-5px;right:-5px;bottom:0;height:2px;background:var(--accent)}
.main-nav a.is-active::before{content:"";position:absolute;left:50%;bottom:1px;margin-left:-4px;border:4px solid transparent;border-bottom-color:var(--accent)}

.hero{position:absolute;top:80px;left:0;width:1094px;height:400px;overflow:hidden;border-bottom:3px solid var(--rule)}
.hero-photo{position:absolute;inset:0;background:
  radial-gradient(ellipse 300px 320px at 900px 210px,#d9a88a 0%,#c9956f 40%,rgba(220,200,180,0) 75%),
  radial-gradient(ellipse 220px 300px at 260px 220px,#f0c2aa 0%,rgba(245,225,215,0) 70%),
  linear-gradient(180deg,#f7f7f6 0%,#eef0f0 55%,#e6d8c8 75%,#f1ebe6 100%)}
.hero-copy{position:absolute;right:395px;top:140px;text-align:right;font-size:19.5px;line-height:44px;color:var(--muted);width:420px}
.hero-cta{position:absolute;left:556px;top:282px;width:144px;height:39px;background:var(--accent);border:2px solid #a9def5;color:#fff;font-size:16px;text-align:center;line-height:35px;text-decoration:none;letter-spacing:.3px}
.slider-arrow{position:absolute;top:193px;width:43px;height:43px;display:flex;align-items:center;justify-content:center}
.slider-arrow--prev{left:0;background:#cfcfcf}
.slider-arrow--next{right:0;border:1px solid rgba(255,255,255,.7);background:rgba(255,255,255,.1)}

.feature-grid{position:absolute;top:530px;left:0;width:1094px}
.feature{position:absolute;width:230px;margin-left:-115px;text-align:center}
.feature-icon{height:74px;display:flex;align-items:center;justify-content:center}
.feature-title{margin-top:13px;font-size:16.5px;font-weight:600;color:var(--ink)}
.feature-text{margin-top:14px;font-size:12px;line-height:19px;color:var(--text)}
.feature-more{display:block;margin-top:17px;font-size:12px;color:var(--more);text-decoration:none}
.icon-placeholder{border-radius:50%;background:radial-gradient(circle at 40% 35%,#e3f1fe,var(--icon-light) 60%,var(--icon) 100%)}

.site-footer{position:absolute;left:0;top:1091px;width:1094px;height:109px;background:radial-gradient(ellipse 500px 60px at 547px 0,#444,var(--footer) 80%)}
.social-list{position:absolute;left:107px;top:21px;display:flex;gap:11px}
.social-item{width:24px;height:24px;border-radius:2px}
.footer-links{position:absolute;right:100px;top:16px;font-size:11px;color:var(--footer-text)}
.footer-links a{color:var(--footer-text);text-decoration:none}
.footer-links .sep{margin:0 8px}
.footer-legal{position:absolute;right:100px;top:38px;font-size:11px;line-height:18px;color:var(--footer-text);text-align:right}
</style>
</head>
<body>
<header class="site-header">
  <div class="brand-name">Lachlan Reeve</div>
  <div class="brand-tagline">Healer - Helper - Mentor - Friend</div>
  <nav class="main-nav">
    <a class="is-active" href="#">Home</a>
    <a href="#">About Me</a>
    <a href="#">How I can help you</a>
    <a href="#">Contact Me</a>
    <a href="#">FAQ</a>
    <a href="#">Client Stories</a>
    <a href="#">Blog</a>
  </nav>
</header>

<section class="hero">
  <div class="hero-photo" role="img" aria-label="Slide photo: hands gesturing on the left and a smiling girl wearing headphones at a sunny beach on the right"></div>
  <p class="hero-copy">Pellentesque nec faucibus ante. Pha-<br>sellus ac purus mi. Cras consequat, risus<br>porttitor suscipit rhoncus</p>
  <a class="hero-cta" href="#">LEARN MORE</a>
  <a class="slider-arrow slider-arrow--prev" href="#" aria-label="Previous slide">
    <svg width="14" height="18" viewBox="0 0 14 18"><path d="M11 2 L4 9 L11 16" fill="none" stroke="#fff" stroke-width="3.5"/></svg>
  </a>
  <a class="slider-arrow slider-arrow--next" href="#" aria-label="Next slide">
    <svg width="14" height="18" viewBox="0 0 14 18"><path d="M3 2 L10 9 L3 16" fill="none" stroke="#fff" stroke-width="3.5"/></svg>
  </a>
</section>

<main class="feature-grid">
  <article class="feature" style="left:229px;top:0">
    <div class="feature-icon"><div class="icon-placeholder" role="img" aria-label="Illustration of a person" style="width:58px;height:68px;border-radius:40% 40% 45% 45%"></div></div>
    <h2 class="feature-title">About Me</h2>
    <p class="feature-text">Who is this Lachlan Reeve?<br>What's his Story</p>
    <a class="feature-more" href="#">More &gt;&gt;</a>
  </article>
  <article class="feature" style="left:513px;top:0">
    <div class="feature-icon">
      <svg width="80" height="64" viewBox="0 0 80 64"><path d="M40 14 C34 2 14 2 8 14 C2 28 20 44 56 60 C72 40 80 26 74 12 C68 0 48 2 40 14Z" fill="#eaf5ff" stroke="var(--icon)" stroke-width="4" stroke-linejoin="round"/></svg>
    </div>
    <h2 class="feature-title">How I can Help You</h2>
    <p class="feature-text">Given up on feeling better? Let me<br>show you something different...</p>
    <a class="feature-more" href="#">More &gt;&gt;</a>
  </article>
  <article class="feature" style="left:797px;top:0">
    <div class="feature-icon"><div class="icon-placeholder" role="img" aria-label="Friendly round glossy emblem" style="width:68px;height:68px"></div></div>
    <h2 class="feature-title">I have Questions</h2>
    <p class="feature-text">How does all this work? Howlong is<br>a sesion, Howmuch?</p>
    <a class="feature-more" href="#">More &gt;&gt;</a>
  </article>

  <article class="feature" style="left:229px;top:265px">
    <div class="feature-icon"><div class="icon-placeholder" role="img" aria-label="Illustration of a client writing notes" style="width:60px;height:70px;border-radius:42% 42% 30% 30%"></div></div>
    <h2 class="feature-title">Client Stories</h2>
    <p class="feature-text">How have others gone from<br>sad to happy?</p>
    <a class="feature-more" href="#">More &gt;&gt;</a>
  </article>
  <article class="feature" style="left:513px;top:265px">
    <div class="feature-icon">
      <svg width="72" height="62" viewBox="0 0 72 62"><ellipse cx="36" cy="24" rx="34" ry="21" fill="var(--icon)"/><path d="M18 38 L12 58 L32 43Z" fill="var(--icon)"/></svg>
    </div>
    <h2 class="feature-title">Blog</h2>
    <p class="feature-text">Want to know the details of how this<br>all works?</p>
    <a class="feature-more" href="#">More &gt;&gt;</a>
  </article>
  <article class="feature" style="left:797px;top:265px">
    <div class="feature-icon">
      <svg width="56" height="56" viewBox="0 0 56 56"><circle cx="28" cy="28" r="25" fill="none" stroke="var(--icon)" stroke-width="3"/><path d="M28 10 V29 L16 40" fill="none" stroke="var(--icon)" stroke-width="3" stroke-linecap="round"/></svg>
    </div>
    <h2 class="feature-title">Contact Me</h2>
    <p class="feature-text">Your better can start today. Book a<br>time now.</p>
    <a class="feature-more" href="#">More &gt;&gt;</a>
  </article>
</main>

<footer class="site-footer">
  <div class="social-list">
    <span class="social-item" style="background:#3b5a9a" aria-label="Social link"></span>
    <span class="social-item" style="background:#3fb8ea" aria-label="Social link"></span>
    <span class="social-item" style="background:#262626;border:1px solid #555" aria-label="Social link"></span>
    <span class="social-item" style="background:#f0a22e" aria-label="Feed link"></span>
    <span class="social-item" style="background:#c4161c" aria-label="Video link"></span>
    <span class="social-item" style="background:#7f9fb8" aria-label="Email link"></span>
  </div>
  <div class="footer-links"><a href="#">Home</a><span class="sep">|</span><a href="#">About Us</a><span class="sep">|</span><a href="#">Sitemap</a></div>
  <div class="footer-legal">© 2014 &nbsp;Lachlan Reeve.. All rights reserved<br>X2</div>
</footer>
</body>
</html>
```